OKRUVI card Technical Architecture

Hello everyone OKRUVI: It is a consulting firm in Architecture and Construction. I require a card duplexing, sober, elegant, classic but not boring. Update 1: Use the following data for the card. Name: Rodrigo Salcedo Mauricio Quintana Position: COO Twitter: @okruviTB Homepage: okruvi.net home address not include the participation of all thank you.

Target Market(s)

Construction companies, Architects and Consulting Engineers

Industry/Entity Type

Consulting

Contact Information for Business Card

Los campos que debe tener:
Nombre, Cargo, email, homepage y twitter

Font styles to use
Serif
Sans Serif
Other font styles liked:
• Me gustan playfair display, open sans y roboto, pero estoy sujeto a sus propuestas

Requirements
Must have
• Colors: Present combined proposals in white, red, gray and black Update 1: The two names must be clearly differentiated from the two surnames
Nice to have
• They are free to present their best proposals. I will bring them immediate feedback to the extent you can go see their designs. Complete data for card and logo files will give the winner the

```html
<!DOCTYPE html>
<html lang="es">
<head>
<meta charset="utf-8">
<title>OKRUVI – Business Card</title>
<link href="https://fonts.googleapis.com/css2?family=Lato:wght@300;400;700&display=swap" rel="stylesheet">
<style>
  :root {
    --stage-bg: #2b2b2b;
    --card-white: #f7f7f7;
    --red-light: #b0101a;
    --red-dark: #6e0309;
    --brand-red: #a3121c;
    --text-gray: #555555;
    --text-dark: #333333;
    --rule-gray: #9a9a9a;
    --white: #ffffff;
  }
  html, body {
    margin: 0;
    padding: 0;
    width: 1200px;
    height: 873px;
    overflow: hidden;
    background: var(--stage-bg);
    font-family: "Lato", Arial, sans-serif;
  }
  .stage {
    position: relative;
    width: 1200px;
    height: 873px;
  }
  .card {
    position: absolute;
    top: 282px;
    width: 540px;
    height: 309px;
    border-radius: 16px;
    box-shadow: 0 10px 30px rgba(0,0,0,.45);
    overflow: hidden;
  }
  /* ---------- Front ---------- */
  .card--front {
    left: 40px;
    background: var(--card-white);
  }
  .front-logo {
    position: absolute;
    left: 40px;
    top: 110px;
  }
  .brand-mark {
    display: flex;
    align-items: center;
    gap: 10px;
  }
  .brand-dot {
    width: 14px;
    height: 14px;
    border-radius: 50%;
    background: var(--brand-red);
  }
  .brand-name {
    font-weight: 300;
    letter-spacing: 10px;
    margin: 0;
  }
  .front-logo .brand-name {
    font-size: 30px;
    color: var(--text-dark);
  }
  .brand-rule {
    height: 1px;
    background: var(--rule-gray);
    margin: 4px 0 3px;
  }
  .front-logo .brand-rule { background: var(--brand-red); }
  .tagline {
    font-weight: 400;
    text-transform: uppercase;
    margin: 0;
  }
  .front-logo .tagline {
    font-size: 10px;
    letter-spacing: 3.2px;
    color: var(--brand-red);
  }
  .people {
    position: absolute;
    right: 36px;
    top: 38px;
    text-align: right;
  }
  .person { margin-bottom: 14px; }
  .person-name {
    font-size: 16px;
    font-weight: 700;
    color: var(--brand-red);
    margin: 0;
  }
  .person-name .surname { font-weight: 400; }
  .person-role {
    font-size: 10px;
    color: var(--text-gray);
    margin: 2px 0 0;
  }
  .contacts {
    position: absolute;
    left: 40px;
    bottom: 34px;
    list-style: none;
    margin: 0;
    padding: 0;
  }
  .contact {
    display: flex;
    align-items: center;
    gap: 9px;
    font-size: 13px;
    color: var(--text-dark);
    margin-top: 6px;
  }
  .contact svg { width: 12px; height: 12px; fill: var(--brand-red); }
  .social-dot {
    width: 10px;
    height: 10px;
    margin: 1px;
    border-radius: 50%;
    background: var(--brand-red);
  }
  /* ---------- Back ---------- */
  .card--back {
    left: 620px;
    background: radial-gradient(ellipse at 50% 30%, var(--red-light) 0%, var(--red-dark) 90%);
    color: var(--white);
  }
  .back-logo {
    position: absolute;
    left: 50%;
    top: 92px;
    transform: translateX(-50%);
    text-align: center;
  }
  .back-logo .brand-mark { justify-content: center; }
  .back-logo .brand-dot { background: var(--white); width: 18px; height: 18px; }
  .back-logo .brand-name {
    font-size: 48px;
    letter-spacing: 16px;
    color: var(--white);
  }
  .back-logo .brand-rule { background: rgba(255,255,255,.7); }
  .back-logo .tagline {
    font-size: 15px;
    letter-spacing: 5px;
    color: var(--white);
  }
  .website {
    position: absolute;
    left: 0;
    right: 0;
    bottom: 46px;
    text-align: center;
    font-size: 14px;
    font-weight: 700;
    letter-spacing: 2.5px;
    color: #f0dede;
  }
</style>
</head>
<body>
<main class="stage">

  <section class="card card--front" aria-label="Card front">
    <div class="people">
      <div class="person">
        <p class="person-name">Rodrigo <span class="surname">Salcedo</span></p>
        <p class="person-role">CEO</p>
      </div>
      <div class="person">
        <p class="person-name">Mauricio <span class="surname">Quintana</span></p>
        <p class="person-role">CEO</p>
      </div>
    </div>

    <div class="front-logo">
      <div class="brand-mark">
        <span class="brand-dot"></span>
        <p class="brand-name">OKRUVI</p>
      </div>
      <div class="brand-rule"></div>
      <p class="tagline">Arquitectura Técnica</p>
    </div>

    <ul class="contacts">
      <li class="contact"><span class="social-dot"></span>@okruviTB</li>
      <li class="contact">
        <svg viewBox="0 0 24 24" aria-hidden="true"><path d="M6.6 10.8a15.1 15.1 0 0 0 6.6 6.6l2.2-2.2c.3-.3.7-.4 1-.2 1.1.4 2.3.6 3.6.6.6 0 1 .4 1 1V20c0 .6-.4 1-1 1A17 17 0 0 1 3 4c0-.6.4-1 1-1h3.5c.6 0 1 .4 1 1 0 1.3.2 2.5.6 3.6.1.3 0 .7-.2 1z"/></svg>
        412-555-0186
      </li>
      <li class="contact">
        <svg viewBox="0 0 24 24" aria-hidden="true"><path d="M2 5h20v14H2z M4 7v.5l8 5 8-5V7l-8 5z" fill-rule="evenodd"/></svg>
        contactus@okruvi.net
      </li>
    </ul>
  </section>

  <section class="card card--back" aria-label="Card back">
    <div class="back-logo">
      <div class="brand-mark">
        <span class="brand-dot"></span>
        <p class="brand-name">OKRUVI</p>
      </div>
      <div class="brand-rule"></div>
      <p class="tagline">Arquitectura Técnica</p>
    </div>
    <p class="website">www.okruvisolutions.net</p>
  </section>

</main>
</body>
</html>
```